Website Build for Brindle Media

I want to create a new website for my company. I would like it to be simple, eye catching and punchy. It will be a homepage, a filter section on case studies and a section for a wordpress blog.
Attached is a non-designed image of what I am thinking for the homepage, in terms of structure and wording.
Also attached is an example white paper, so we can follow a similar colour scheme.
Coding
Number of Pages Required
Look and feel

```html
<!DOCTYPE html>
<html lang="en">
<head>
<meta charset="utf-8">
<title>Brindle Media — Visionary Media Strategies</title>
<link rel="stylesheet" href="https://fonts.googleapis.com/css2?family=Poppins:wght@300;400;500;600;700&display=swap">
<style>
:root{
  --orange:#ff7a00;
  --orange-deep:#f5570f;
  --amber:#ffb400;
  --yellow:#ffc800;
  --red:#f04a2a;
  --ink:#2b2b2b;
  --muted:#6b6b6b;
  --line:#e2e2e2;
  --dark:#343434;
  --white:#ffffff;
  --green:#2fae6b;
}
*{box-sizing:border-box;margin:0;padding:0}
html,body{width:1200px;height:4648px;overflow:hidden}
body{font-family:"Poppins",sans-serif;color:var(--ink);background:var(--white);position:relative}
.abs{position:absolute}
.ph{position:absolute}
a{color:inherit;text-decoration:none}

/* Hero */
.hero-shape{left:0;top:0;width:712px;height:592px;background:linear-gradient(120deg,var(--orange-deep) 0%,var(--orange) 45%,var(--yellow) 100%);border-bottom-right-radius:60px;clip-path:polygon(0 0,470px 0,712px 430px,712px 592px,0 592px)}
.hero-photo{left:700px;top:0;width:500px;height:592px;background:linear-gradient(160deg,#f2f2f2,#ff8a1a 60%,#e0661a);border-bottom-left-radius:70px}
.play{width:74px;height:74px;border-radius:50%;background:var(--white);display:flex;align-items:center;justify-content:center;box-shadow:0 6px 20px rgba(0,0,0,.2)}
.logo{font-weight:700;font-size:26px;color:var(--white)}
.nav{top:20px;left:676px;display:flex;gap:22px;font-size:13px;font-weight:500;color:var(--ink)}
.btn{display:inline-flex;align-items:center;justify-content:center;font-weight:600;font-size:13px;border-radius:8px}
.btn-contact{left:982px;top:10px;width:128px;height:40px;background:var(--red);color:var(--white)}
.hero-title{left:88px;top:232px;color:var(--white)}
.hero-title strong{display:block;font-size:50px;font-weight:700;line-height:1.15}
.hero-title span{display:block;font-size:41px;font-weight:300;line-height:1.3}
.btn-ghost{left:88px;top:418px;width:170px;height:40px;border:2px solid var(--white);color:var(--white)}

/* Features */
.feature{top:682px;width:230px;text-align:center}
.feature .icon{width:78px;height:66px;margin:0 auto 18px;border-radius:6px}
.feature h3{font-size:18px;font-weight:600;margin-bottom:8px}
.feature p{font-size:12px;line-height:1.65;color:var(--muted)}
.divider-v{width:2px;background:#bdbdbd;top:670px;height:255px}

/* Section headings */
.eyebrow{font-size:16px;font-weight:600;color:var(--orange-deep)}
.h2{font-size:40px;font-weight:400;line-height:1.2}
.h2 b{font-weight:700}
.body{font-size:12px;line-height:1.8;color:var(--muted)}

/* About */
.about-shape{left:0;top:955px;width:380px;height:720px;background:linear-gradient(150deg,var(--orange-deep),var(--red));clip-path:polygon(45% 0,80% 0,100% 15%,100% 85%,50% 100%,0 90%,0 15%)}
.about-photo{left:107px;top:1070px;width:476px;height:490px;background:linear-gradient(160deg,#f3f3f3,#d88a3a 65%,#5c5c5c);border-top-left-radius:70px;border-bottom-right-radius:120px}
.btn-red{background:var(--red);color:var(--white)}

/* Case studies */
.case-circle{width:190px;height:190px;border-radius:50%;background:var(--white);box-shadow:0 8px 28px rgba(0,0,0,.09);display:flex;align-items:center;justify-content:center;font-weight:700;font-size:17px}
.case-name{font-size:17px;font-weight:500;text-align:center;width:190px}
.case-card{left:335px;top:1876px;width:330px;height:272px;background:var(--white);border-radius:10px;box-shadow:0 10px 30px rgba(0,0,0,.1);text-align:center;padding:10px}
.case-card .thumb{height:126px;background:#e6e6e6;border-radius:10px;display:flex;align-items:center;justify-content:center;gap:10px;font-size:22px;font-weight:500}
.arrow{width:40px;height:40px;border-radius:50%;background:linear-gradient(135deg,var(--orange),var(--red));display:flex;align-items:center;justify-content:center}

/* Why */
.why-shape{left:900px;top:2260px;width:300px;height:770px;background:linear-gradient(170deg,var(--yellow),var(--orange));clip-path:polygon(45% 0,100% 0,100% 100%,30% 75%,0 30%)}
.why-photo{left:614px;top:2373px;width:476px;height:539px;background:linear-gradient(160deg,#cfd8e4,#b59a6a 55%,#59606e);border-top-right-radius:70px;border-bottom-left-radius:140px}
.stat-num{font-size:42px;font-weight:500;line-height:1}
.stat-label{font-size:19px;margin-top:10px}

/* Partners */
.partner{width:186px;height:186px;border-radius:50%;background:var(--white);box-shadow:0 8px 28px rgba(0,0,0,.09);display:flex;flex-direction:column;align-items:center;justify-content:center;gap:8px;font-size:13px;font-weight:600;color:#444}
.dot{width:36px;height:36px;border-radius:50%}

/* Blog */
.card{top:3437px;width:276px;height:303px;border:1px solid var(--line);border-radius:8px;overflow:hidden;background:var(--white)}
.card .img{height:163px;background:linear-gradient(150deg,#c9c3b7,#7a6d5e 60%,#3f3a36)}
.card .txt{padding:12px 14px}
.card h4{font-size:17px;font-weight:600;line-height:1.3;margin-bottom:6px}
.card p{font-size:12px;line-height:1.65;color:var(--muted)}

/* Contact */
.footer-bg{left:0;top:4214px;width:1200px;height:434px;background:var(--dark)}
.contact-box{left:200px;top:3843px;width:796px;height:430px;border-radius:28px;background:linear-gradient(110deg,var(--orange-deep),#fa8454 60%,#ffa27a)}
.contact-photo{left:245px;top:3896px;width:328px;height:322px;border-radius:24px;background:linear-gradient(150deg,#8a7a62,#5f5140 55%,#2d2a28)}
.field{background:var(--white);border-radius:16px;height:30px;font-size:11px;color:#888;padding:7px 14px}
.contact-title{left:604px;top:3910px;color:var(--white);font-size:32px;font-weight:300}
.contact-title b{font-weight:600}

/* Footer */
.f-head{font-size:22px;color:var(--white);font-weight:400}
.f-list{font-size:12px;color:var(--white);line-height:2.25}
.social{width:42px;height:42px;border-radius:50%;background:var(--orange)}
.f-bottom{left:88px;top:4584px;width:1024px;height:1px;background:#777}
</style>
</head>
<body>

<!-- Hero -->
<div class="ph hero-shape"></div>
<div class="ph hero-photo" role="img" aria-label="Photo of a smiling man working on a laptop in an orange armchair"></div>
<div class="abs play" style="left:874px;top:285px">
  <svg width="22" height="24" viewBox="0 0 22 24"><path d="M2 1l19 11L2 23z" fill="var(--orange)"/></svg>
</div>
<div class="abs logo" style="left:88px;top:12px">Logo Here</div>
<nav class="abs nav"><a>Home</a><a>About Us</a><a>Case Studies</a><a>Blog</a></nav>
<a class="abs btn btn-contact">Contact Us</a>
<h1 class="abs hero-title"><strong>Driving Business</strong><span>Change with Visionary<br>Media Strategies.</span></h1>
<a class="abs btn btn-ghost">Get Started Now</a>

<!-- Features -->
<div class="abs feature" style="left:112px">
  <div class="icon" style="background:#d9ecff"><svg width="78" height="66" viewBox="0 0 78 66"><circle cx="39" cy="33" r="18" fill="none" stroke="#2a8be0" stroke-width="4"/><path d="M21 33h36M39 15v36" stroke="#2a8be0" stroke-width="3"/></svg></div>
  <h3>Global Reach</h3>
  <p>It is a long established fact that a reader will be distracted by the readable content of a page when looking at its layout.</p>
</div>
<div class="abs divider-v" style="left:374px"></div>
<div class="abs feature" style="left:455px">
  <div class="icon" style="background:#dcf5e4"><svg width="78" height="66" viewBox="0 0 78 66"><rect x="22" y="36" width="7" height="16" fill="var(--green)"/><rect x="34" y="28" width="7" height="24" fill="var(--green)"/><rect x="46" y="20" width="7" height="32" fill="var(--green)"/></svg></div>
  <h3>Driven Media Strategies</h3>
  <p>It is a long established fact that a reader will be distracted by the readable content of a page when looking at its layout.</p>
</div>
<div class="abs divider-v" style="left:766px"></div>
<div class="abs feature" style="left:828px">
  <div class="icon" style="background:#ffe2cf"><svg width="78" height="66" viewBox="0 0 78 66"><circle cx="39" cy="28" r="12" fill="var(--orange)"/><rect x="34" y="42" width="10" height="8" fill="var(--orange)"/></svg></div>
  <h3>Visionary Approach</h3>
  <p>It is a long established fact that a reader will be distracted by the readable content of a page when looking at its layout.</p>
</div>

<!-- About -->
<div class="ph about-shape"></div>
<div class="ph about-photo" role="img" aria-label="Photo of a smiling woman in an orange sweater holding a tablet"></div>
<div class="abs" style="left:642px;top:1130px;width:410px">
  <div class="eyebrow">About Us</div>
  <h2 class="h2" style="margin:6px 0 16px"><b>Who</b> We Are</h2>
  <p class="body" style="margin-bottom:12px">At Brindle Media, we are more than just a media agency—we are partners in change. We collaborate with forward-thinking brands to create strategies that deliver measurable business impact.</p>
  <p class="body">Welcome to Brindle, where we run digital Marketing campaigns with influ ence market ing at the heart and deliver real results we can help with your digital Marketing.</p>
</div>
<a class="abs btn btn-red" style="left:642px;top:1380px;width:128px;height:38px">Learn More</a>

<!-- Case Study -->
<div class="abs" style="left:0;top:1712px;width:1200px;text-align:center">
  <div class="eyebrow">Case Study</div>
  <h2 class="h2" style="margin:6px 0 10px"><b>Our Work</b> in Action</h2>
  <p class="body" style="width:700px;margin:0 auto;color:#555">Filters: Provide filters to let users narrow down the case studies by categories such as 'Behavior Change,' 'B2B,' 'Culture,' and 'Retail</p>
</div>
<div class="abs arrow" style="left:68px;top:1997px"><svg width="16" height="16" viewBox="0 0 16 16"><path d="M14 8H2M7 3L2 8l5 5" stroke="#fff" stroke-width="2" fill="none"/></svg></div>
<div class="abs case-circle" style="left:134px;top:1876px;color:#b48a2e">Fernleaf</div>
<div class="abs case-name" style="left:139px;top:2082px">Fernleaf</div>
<div class="abs case-card">
  <div class="thumb"><span style="width:36px;height:36px;border-radius:50%;background:var(--orange)"></span>Voltline</div>
  <h4 style="font-size:17px;font-weight:500;margin:14px 0 4px">Voltline</h4>
  <p style="font-size:12px;line-height:2;color:#444">Discover how we increased Voltline's social media engagement by 150% in just six months through a dynamic content strategy.</p>
</div>
<div class="abs case-circle" style="left:677px;top:1876px;color:#1b6fc0">Carewell</div>
<div class="abs case-name" style="left:682px;top:2082px">Carewell</div>
<div class="abs case-circle" style="left:876px;top:1876px;color:#111">Threadly</div>
<div class="abs case-name" style="left:881px;top:2082px">Threadly</div>
<div class="abs arrow" style="left:1090px;top:1997px"><svg width="16" height="16" viewBox="0 0 16 16"><path d="M2 8h12M9 3l5 5-5 5" stroke="#fff" stroke-width="2" fill="none"/></svg></div>

<!-- Why Choose Us -->
<div class="ph why-shape"></div>
<div class="ph why-photo" role="img" aria-label="Photo of a woman in a mustard shirt holding a tablet in a bright office"></div>
<div class="abs" style="left:88px;top:2415px;width:400px">
  <div class="eyebrow">Differentiator</div>
  <h2 class="h2" style="margin:6px 0 24px"><b>Why</b> Choose Us?</h2>
  <p style="font-size:12px;font-weight:600;color:#444;margin-bottom:14px">A few bold statements that set your agency apart.</p>
  <p class="body">Doing what everyone else does will get you the same results as everyone else.</p>
</div>
<div class="abs" style="left:248px;top:2610px;width:1px;height:120px;background:var(--line)"></div>
<div class="abs" style="left:248px;top:2765px;width:1px;height:120px;background:var(--line)"></div>
<div class="abs" style="left:88px;top:2747px;width:356px;height:1px;background:var(--line)"></div>
<div class="abs" style="left:88px;top:2622px"><div class="stat-num" style="color:var(--orange)">250</div><div class="stat-label">Projects Done</div></div>
<div class="abs" style="left:300px;top:2622px"><div class="stat-num" style="color:#1e7ad6">70+</div><div class="stat-label">Consultants</div></div>
<div class="abs" style="left:88px;top:2773px"><div class="stat-num" style="color:var(--green)">250</div><div class="stat-label">Awards Won</div></div>
<div class="abs" style="left:300px;top:2773px"><div class="stat-num">150+</div><div class="stat-label">Happy Clients</div></div>

<!-- Partners -->
<div class="abs partner" style="left:198px;top:3006px"><span class="dot" style="background:#1e7ad6"></span>LOGO TEXT</div>
<div class="abs partner" style="left:412px;top:3006px"><span class="dot" style="background:#7b2fbf"></span>ABSTRACT LOGO</div>
<div class="abs partner" style="left:612px;top:3006px"><span class="dot" style="background:#e8b020"></span>LOREM IPSUM</div>
<div class="abs partner" style="left:817px;top:3006px"><span class="dot" style="background:#e23a6a"></span>Business Name</div>

<!-- Resources -->
<div class="abs" style="left:0;top:3285px;width:1200px;text-align:center">
  <div class="eyebrow">Resources and Insights</div>
  <h2 class="h2" style="margin:6px 0 12px"><b>Marketing</b> Resources <b>&amp;</b> Insights</h2>
  <p class="body" style="color:#555">Explore our blog for tips, insights, and trends that help deliver outstanding marketing.</p>
</div>
<article class="abs card" style="left:156px">
  <div class="img" role="img" aria-label="Photo of colleagues reviewing charts on a laptop"></div>
  <div class="txt"><h4>some blog heading goes here</h4><p>It is a long established fact that a reader will be distracted by the readable content layout...</p></div>
</article>
<article class="abs card" style="left:461px">
  <div class="img" role="img" aria-label="Photo of a team meeting around an office table"></div>
  <div class="txt"><h4>some blog heading goes here</h4><p>It is a long established fact that a reader will be distracted by the readable content layout...</p></div>
</article>
<article class="abs card" style="left:767px">
  <div class="img" role="img" aria-label="Photo of two colleagues discussing work at a desk"></div>
  <div class="txt"><h4>some blog heading goes here</h4><p>It is a long established fact that a reader will be distracted by the readable content layout...</p></div>
</article>

<!-- Contact -->
<div class="ph footer-bg"></div>
<div class="ph contact-box"></div>
<div class="ph contact-photo" role="img" aria-label="Photo of a smiling man using his phone at a desk"></div>
<div class="abs" style="left:385px;top:4034px;width:46px;height:46px;border-radius:50%;border:3px solid #fff;display:flex;align-items:center;justify-content:center"><svg width="14" height="16" viewBox="0 0 14 16"><path d="M2 1l11 7-11 7z" fill="#fff"/></svg></div>
<h2 class="abs contact-title"><b>Get In</b> Touch With Us</h2>
<div class="abs field" style="left:604px;top:3978px;width:164px">Name*</div>
<div class="abs field" style="left:778px;top:3978px;width:164px">Phone*</div>
<div class="abs field" style="left:604px;top:4020px;width:338px">Email*</div>
<div class="abs field" style="left:604px;top:4062px;width:338px;height:92px;border-radius:14px">Send Message*</div>
<a class="abs btn" style="left:604px;top:4168px;width:118px;height:36px;background:#fff;color:var(--ink);border-radius:18px">Let's Talk</a>

<!-- Footer -->
<div class="abs" style="left:103px;top:4375px;font-size:34px;font-weight:500;color:#fff">Logo Here</div>
<div class="abs" style="left:90px;top:4432px;display:flex;gap:10px">
  <span class="social"></span><span class="social" style="background:#666"></span><span class="social" style="background:#666"></span><span class="social" style="background:#666"></span>
</div>
<div class="abs" style="left:370px;top:4332px">
  <div class="f-head" style="margin-bottom:8px">Quick links</div>
  <div class="f-list">Home<br>About Us<br>Contact<br>Case Studies<br>Blog</div>
</div>
<div class="abs" style="left:582px;top:4332px;width:220px">
  <div class="f-head" style="margin-bottom:12px">Contact info</div>
  <div class="f-list" style="line-height:1.5">
    <div style="display:flex;gap:8px;margin-bottom:14px"><span style="width:12px;height:9px;background:var(--orange);margin-top:4px"></span><span>Email:<br>email@example.com</span></div>
    <div style="display:flex;gap:8px;margin-bottom:14px"><svg width="12" height="12" viewBox="0 0 12 12"><path d="M2 1l3 0 1 3-2 1a7 7 0 003 3l1-2 3 1v3C6 11 1 6 2 1z" fill="var(--orange)"/></svg><span>Phone:<br>0123.456.789</span></div>
    <div style="display:flex;gap:8px"><svg width="12" height="14" viewBox="0 0 12 14"><path d="M6 0a5 5 0 00-5 5c0 4 5 9 5 9s5-5 5-9a5 5 0 00-5-5z" fill="var(--orange)"/></svg><span>Location:<br>Some address line here<br>United Kingdom ZX9 4QT</span></div>
  </div>
</div>
<div class="abs" style="left:847px;top:4332px;width:265px">
  <div class="f-head" style="margin-bottom:10px">Newsletter</div>
  <p style="font-size:12px;color:#fff;line-height:1.5;margin-bottom:16px">Subscribe to our email address to get the latest news.</p>
  <div style="background:#fff;border-radius:22px;height:44px;display:flex;align-items:center;padding:0 16px;gap:10px;font-size:11px;color:#555">
    <span style="width:12px;height:9px;background:var(--orange)"></span><span style="flex:1">Enter your email...</span>
    <svg width="20" height="18" viewBox="0 0 20 18"><path d="M1 8L19 1 14 17 10 11z" fill="var(--orange)"/></svg>
  </div>
</div>
<div class="abs f-bottom"></div>
<div class="abs" style="left:0;top:4612px;width:1200px;text-align:center;font-size:13px;color:#fff">© Copyright 2024 | All Right Reserveds</div>

</body>
</html>
```